Business Card - connecting 2 souls and beggining the journey of self discovery

Logo on the front
with tag line

On the back list of services and contact details

Seminars
workshops
Coaching
podcasts

Daniel Porthwick
Health & Wellbeing Life Coach
0491 372 815
daniel@wovenpathwellness.example
wovenpathwellness.example

Industry/Entity Type

Life Coaching

Contact Information for Business Card

I like the use of colour from the logo to be used. I'm not a fan of white.

Requirements
Must have
• My tagline: The journey home starts with you
Nice to have
• Use of colour that is in the mind body soul logo

```html
<!DOCTYPE html>
<html lang="en">
<head>
<meta charset="utf-8">
<title>Woven Path Wellness — Business Card</title>
<link rel="stylesheet" href="https://fonts.googleapis.com/css2?family=Open+Sans:wght@400;600&family=Roboto:wght@400;500&family=Roboto+Condensed:wght@700&display=swap">
<style>
  :root {
    --backdrop: #2b2b2b;
    --card: #f1f1f1;
    --band-grey: #7b7b7d;
    --ink-grey: #6f6f71;
    --ink-dark: #4a4a4a;
    --white: #ffffff;
    --purple: #9a4cc4;
    --pink: #ef6f7e;
    --orange: #f4b545;
    --green: #6cc07a;
    --teal: #3bb5a4;
  }
  * { box-sizing: border-box; margin: 0; padding: 0; }
  html, body { width: 1200px; height: 960px; overflow: hidden; }
  body { background: var(--backdrop); position: relative; font-family: "Open Sans", sans-serif; }

  .card {
    position: absolute;
    width: 600px;
    height: 342px;
    border-radius: 22px;
    background: var(--card);
    overflow: hidden;
  }
  .card--front { left: 314px; top: 114px; }
  .card--back  { left: 311px; top: 473px; }

  /* Front */
  .brand-mark {
    position: absolute; left: 262px; top: 34px;
    width: 78px; height: 78px; border-radius: 50%;
    background: var(--teal);
  }
  .brand-name {
    position: absolute; left: 0; right: 0; top: 126px;
    text-align: center; font-size: 21px; font-weight: 400;
    letter-spacing: -0.6px; color: var(--ink-grey);
  }
  .tagline {
    position: absolute; left: 0; right: 0; top: 151px;
    text-align: center; font-size: 13px; font-weight: 600;
    color: var(--ink-grey);
  }
  .band { position: absolute; left: 0; top: 0; width: 600px; height: 342px; }

  .holder { position: absolute; left: 33px; top: 259px; color: var(--white); }
  .holder__name {
    font-family: "Roboto Condensed", sans-serif;
    font-size: 21px; font-weight: 700; letter-spacing: 0.2px; line-height: 26px;
  }
  .holder__role {
    font-family: "Roboto", sans-serif;
    font-size: 13px; font-weight: 500; letter-spacing: 0.1px;
  }

  .contact {
    position: absolute; left: 329px; top: 260px; list-style: none;
    font-family: "Roboto", sans-serif; font-size: 14px; color: var(--white);
  }
  .contact li { display: flex; align-items: center; height: 19px; }
  .contact svg { width: 13px; height: 13px; margin-right: 9px; flex: none; }

  /* Back */
  .back-mark {
    position: absolute; left: 245px; top: 84px;
    width: 110px; height: 110px; border-radius: 50%;
    background: var(--teal);
  }
  .back-name {
    position: absolute; left: 0; right: 0; top: 206px;
    text-align: center; font-size: 21px; font-weight: 400;
    letter-spacing: -0.6px; color: var(--ink-grey);
  }
  .services {
    position: absolute; left: 0; right: 0; top: 301px;
    text-align: center; font-family: "Roboto", sans-serif;
    font-size: 15px; color: var(--ink-dark);
  }
  .services .dot { color: var(--teal); margin: 0 2px; font-size: 10px; vertical-align: 1px; }
</style>
</head>
<body>

<section class="card card--front">
  <div class="brand-mark"></div>
  <p class="brand-name">Woven Path Wellness</p>
  <p class="tagline">The journey home starts with you</p>

  <svg class="band" viewBox="0 0 600 342" role="img" aria-label="Soft colour accent above the grey contact band">
    <defs>
      <linearGradient id="accent" x1="0" y1="0" x2="600" y2="0" gradientUnits="userSpaceOnUse">
        <stop offset="0" stop-color="var(--purple)"/>
        <stop offset="0.35" stop-color="var(--pink)"/>
        <stop offset="0.65" stop-color="var(--orange)"/>
        <stop offset="1" stop-color="var(--green)"/>
      </linearGradient>
    </defs>
    <path d="M0,222 C160,200 380,206 600,186 L600,226 C380,236 160,224 0,236 Z" fill="url(#accent)" opacity="0.85"/>
    <path d="M0,236 C160,224 380,236 600,226 L600,342 L0,342 Z" fill="var(--band-grey)"/>
  </svg>

  <div class="holder">
    <p class="holder__name">DANIEL PORTHWICK</p>
    <p class="holder__role">HEALTH &amp; WELLBEING LIFE COACH</p>
  </div>

  <ul class="contact">
    <li>
      <svg viewBox="0 0 24 24"><path fill="var(--white)" d="M6.6 10.8a15.1 15.1 0 0 0 6.6 6.6l2.2-2.2a1 1 0 0 1 1-.25 11.4 11.4 0 0 0 3.6.57 1 1 0 0 1 1 1V20a1 1 0 0 1-1 1A17 17 0 0 1 3 4a1 1 0 0 1 1-1h3.5a1 1 0 0 1 1 1c0 1.25.2 2.45.57 3.57a1 1 0 0 1-.25 1z"/></svg>
      0491 372 815
    </li>
    <li>
      <svg viewBox="0 0 24 24"><rect x="2" y="5" width="20" height="14" fill="var(--white)"/><path d="M2 6l10 7 10-7" fill="none" stroke="var(--band-grey)" stroke-width="2"/></svg>
      daniel@wovenpathwellness.example
    </li>
    <li>
      <svg viewBox="0 0 24 24"><circle cx="12" cy="12" r="10" fill="var(--white)"/><path d="M2 12h20M12 2c3 3 3 17 0 20M12 2c-3 3-3 17 0 20" fill="none" stroke="var(--band-grey)" stroke-width="1.6"/></svg>
      www.wovenpathwellness.example
    </li>
  </ul>
</section>

<section class="card card--back">
  <div class="back-mark"></div>
  <p class="back-name">Woven Path Wellness</p>
  <p class="services">
    Seminars <span class="dot">●</span> Workshops <span class="dot">●</span> Coaching <span class="dot">●</span> Podcasts
  </p>
</section>

</body>
</html>
```